Golden Pantry Spice

Distributor of seasonings and spices to the restaurant industry.

Industry/Entity Type

Restaurant

Contact Information for Business Card

Golden Pantry
Derek Hollings
TW Brandvik Distributor
316-487-9021
derek@goldpantryspicehub.com

No minimum order
Gluten & MSG free soup bases

```html
<!DOCTYPE html>
<html lang="en">
<head>
<meta charset="utf-8">
<title>Golden Pantry Spice – Business Card</title>
<link rel="stylesheet" href="https://fonts.googleapis.com/css2?family=Source+Sans+3:wght@400;600&display=swap">
<style>
  :root {
    --backdrop: #1c1c1c;
    --card-white: #ffffff;
    --card-grey: #6b6663;
    --tab-dark: #333534;
    --brand-dark: #3b3230;
    --accent-orange: #ef6c4a;
    --text-dark: #2a2a2a;
    --icon-gold: #b59a3c;
    --text-light: #ffffff;
  }
  * { margin: 0; padding: 0; box-sizing: border-box; }
  html, body {
    width: 1200px; height: 900px; overflow: hidden;
    background: var(--backdrop);
    font-family: "Source Sans 3", "Myriad Pro", Arial, sans-serif;
  }
  .canvas { position: relative; width: 1200px; height: 900px; }

  .card {
    position: absolute; top: 170px; width: 347px; height: 561px;
    text-align: center;
  }
  .card-front { left: 259px; background: var(--card-white); }
  .card-back  { left: 631px; background: var(--card-grey); }

  .tab {
    position: absolute; left: 102px; width: 143px;
    background: var(--tab-dark);
  }
  .tab-top { top: 0; height: 30px; }
  .tab-bottom { bottom: 0; height: 28px; }

  .brand-name {
    position: absolute; left: 0; right: 0;
    color: var(--brand-dark); font-weight: 600;
    font-size: 34px; line-height: 38px;
  }
  .card-front .brand-name { top: 104px; }
  .card-back .brand-name { top: 198px; }

  .holder-name {
    position: absolute; top: 286px; left: 0; right: 0;
    color: var(--accent-orange); font-weight: 600; font-size: 19px;
  }
  .holder-role {
    position: absolute; top: 309px; left: 0; right: 0;
    color: var(--text-dark); font-size: 15px;
  }
  .contact {
    position: absolute; left: 0; right: 0;
    color: var(--text-dark); font-size: 15px;
    display: flex; justify-content: center; align-items: center; gap: 7px;
  }
  .contact-phone { top: 396px; }
  .contact-email { top: 419px; }
  .contact svg { flex: none; }

  .selling-points {
    position: absolute; top: 477px; left: 0; right: 0;
    color: var(--text-light); font-weight: 600; font-size: 17px; line-height: 23px;
  }
</style>
</head>
<body>
<div class="canvas">
  <section class="card card-front">
    <div class="tab tab-top"></div>
    <div class="brand-name">Golden Pantry<br>Spice</div>
    <div class="holder-name">Derek Hollings</div>
    <div class="holder-role">TW Brandvik Distributor</div>
    <div class="contact contact-phone">
      <svg width="8" height="12" viewBox="0 0 8 12" aria-hidden="true">
        <rect x="0.75" y="0.75" width="6.5" height="10.5" rx="1.2" fill="none" stroke="var(--icon-gold)" stroke-width="1.5"/>
        <rect x="3" y="9" width="2" height="1" fill="var(--icon-gold)"/>
      </svg>
      <span>316-487-9021</span>
    </div>
    <div class="contact contact-email">
      <svg width="10" height="7" viewBox="0 0 10 7" aria-hidden="true">
        <rect width="10" height="7" fill="var(--icon-gold)"/>
        <polyline points="0,0 5,4 10,0" fill="none" stroke="#fff" stroke-width="1"/>
      </svg>
      <span>derek@goldpantryspicehub.com</span>
    </div>
    <div class="tab tab-bottom"></div>
  </section>

  <section class="card card-back">
    <div class="brand-name">Golden Pantry<br>Spice</div>
    <div class="selling-points">No minimum order<br>Gluten &amp; MSG free soup bases</div>
  </section>
</div>
</body>
</html>
```